" Quintela advogados é um escritório de advocacia de grande porte atuando em 6 Estados, sendo em 3 deles temos filial em funcionamento, além da matriz (Curitiba). "

```html
<!DOCTYPE html>
<html lang="pt-BR">
<head>
<meta charset="utf-8">
<title>Quintela advogados — cartão de visita</title>
<link rel="stylesheet" href="https://fonts.googleapis.com/css2?family=Cinzel:wght@500&family=Exo+2:wght@400;600&display=swap">
<style>
  :root {
    --page: #e9e5df;
    --card-dark: #1c2329;
    --card-mid: #2a3239;
    --gold-light: #f6d77a;
    --gold: #d6a63c;
    --gold-deep: #9a6a18;
    --text-light: #f2f2f2;
    --text-muted: #b9bec3;
    --divider: #d9dde0;
  }
  * { box-sizing: border-box; margin: 0; padding: 0; }
  html, body { width: 1200px; height: 1200px; overflow: hidden; }
  body {
    background: var(--page);
    font-family: "Exo 2", sans-serif;
    position: relative;
  }
  .card {
    position: absolute;
    left: 259px;
    width: 682px;
    height: 391px;
    background: linear-gradient(160deg, var(--card-mid) 0%, var(--card-dark) 60%);
    box-shadow: 0 10px 24px rgba(0,0,0,.25);
    overflow: hidden;
  }
  .card--front { top: 156px; }
  .card--back { top: 600px; }
  .band {
    position: absolute;
    left: 0; right: 0;
    background: linear-gradient(90deg, var(--gold-deep), var(--gold-light) 30%, var(--gold) 55%, var(--gold-light) 80%, var(--gold-deep));
  }
  .band--top { top: 0; height: 10px; }
  .band--bottom { bottom: 0; height: 16px; }

  .brand {
    position: absolute;
    left: 0; right: 0;
    top: 150px;
    display: flex;
    flex-direction: column;
    align-items: center;
    gap: 26px;
  }
  .brand__square {
    width: 26px; height: 26px;
    background: var(--gold);
  }
  .brand__name {
    font-family: "Cinzel", serif;
    font-weight: 500;
    font-size: 44px;
    letter-spacing: 3px;
    color: var(--gold-light);
  }

  .back-brand {
    position: absolute;
    left: 0; width: 300px;
    top: 150px;
    display: flex;
    flex-direction: column;
    align-items: center;
    gap: 14px;
  }
  .back-brand__square { width: 20px; height: 20px; background: var(--gold); }
  .back-brand__name {
    font-family: "Cinzel", serif;
    font-weight: 500;
    font-size: 24px;
    color: var(--gold-light);
    text-align: center;
    line-height: 1.3;
  }
  .divider {
    position: absolute;
    left: 300px; top: 48px;
    width: 2px; height: 284px;
    background: var(--divider);
  }
  .contact {
    position: absolute;
    left: 360px; top: 44px;
    color: var(--text-light);
  }
  .contact__name { font-weight: 600; font-size: 28px; line-height: 1.1; }
  .contact__role { font-size: 19px; color: var(--text-muted); margin-bottom: 26px; }
  .contact__list { list-style: none; }
  .contact__item {
    display: flex; align-items: center; gap: 10px;
    font-size: 16px; height: 26px;
  }
  .contact__gap { height: 18px; }
  .icon { width: 18px; height: 18px; flex: none; }
</style>
</head>
<body>
  <section class="card card--front" aria-label="Frente do cartão">
    <div class="band band--top"></div>
    <div class="brand">
      <div class="brand__square"></div>
      <div class="brand__name">Quintela advogados</div>
    </div>
    <div class="band band--bottom"></div>
  </section>

  <section class="card card--back" aria-label="Verso do cartão">
    <div class="band band--top"></div>
    <div class="back-brand">
      <div class="back-brand__square"></div>
      <div class="back-brand__name">Quintela<br>advogados</div>
    </div>
    <div class="divider"></div>
    <div class="contact">
      <p class="contact__name">Nome Sobrenome</p>
      <p class="contact__role">cargo</p>
      <ul class="contact__list">
        <li class="contact__item">
          <svg class="icon" viewBox="0 0 20 20"><circle cx="10" cy="10" r="9" fill="#d6a63c"/><path d="M7 5.5l2 2-1 1.3c.7 1.4 1.8 2.5 3.2 3.2l1.3-1 2 2-1.2 1.5C9.8 14 6 10.2 5.5 6.7z" fill="#1c2329"/></svg>
          +55 37 8888-9999
        </li>
        <li class="contact__item">
          <svg class="icon" viewBox="0 0 20 20"><circle cx="10" cy="10" r="9" fill="#d6a63c"/><path d="M7 5.5l2 2-1 1.3c.7 1.4 1.8 2.5 3.2 3.2l1.3-1 2 2-1.2 1.5C9.8 14 6 10.2 5.5 6.7z" fill="#1c2329"/></svg>
          +55 37 8888-9999
        </li>
        <li class="contact__gap"></li>
        <li class="contact__item">
          <svg class="icon" viewBox="0 0 20 20"><rect x="2" y="4" width="16" height="12" rx="2" fill="#d6a63c"/><path d="M3 5l7 6 7-6" fill="none" stroke="#1c2329" stroke-width="1.6"/></svg>
          contato@contato.com.br
        </li>
        <li class="contact__item">
          <svg class="icon" viewBox="0 0 20 20"><circle cx="10" cy="10" r="8" fill="#d6a63c"/><g fill="none" stroke="#1c2329" stroke-width="1.2"><ellipse cx="10" cy="10" rx="3.5" ry="8"/><path d="M2 10h16M3.5 6h13M3.5 14h13"/></g></svg>
          www.site.com.br
        </li>
        <li class="contact__gap"></li>
        <li class="contact__item">
          <svg class="icon" viewBox="0 0 20 20"><path d="M10 1.5a6 6 0 0 1 6 6c0 4.5-6 11-6 11s-6-6.5-6-11a6 6 0 0 1 6-6z" fill="#d6a63c"/><circle cx="10" cy="7.5" r="2.2" fill="#1c2329"/></svg>
          Endereço: Exemplo - N 11
        </li>
        <li class="contact__item">
          <svg class="icon" viewBox="0 0 20 20"><circle cx="10" cy="10" r="8" fill="#d6a63c"/></svg>
          instagram/id
        </li>
        <li class="contact__item">
          <svg class="icon" viewBox="0 0 20 20"><circle cx="10" cy="10" r="8" fill="#d6a63c"/></svg>
          facebook/id
        </li>
      </ul>
    </div>
    <div class="band band--bottom"></div>
  </section>
</body>
</html>
```